Visitenkarten-Design für Metzgerei
Zielgruppe
Metzgerei, Fleischsommelier
Zielgruppe: BBQ Szene
Aufgabenstellung
Visitenkarte gefalzt, Grundfarbe schwarz, mit unserem Logo, Foto sowie Sommelier-Logo
Standartangaben wie Internetadresse, Instagram,

```html
<!DOCTYPE html>
<html lang="de">
<head>
<meta charset="utf-8">
<title>Visitenkarte Metzgerei Brenner</title>
<link href="https://fonts.googleapis.com/css2?family=Montserrat:wght@400;600;700&display=swap" rel="stylesheet">
<style>
  :root {
    --bg: #c8cccd;
    --card: #2a2a2b;
    --card-dark: #232324;
    --gold: #f2b705;
    --text: #d9d9d9;
    --muted: #9a9a9a;
    --photo-a: #3a3a3a;
    --photo-b: #8d8d8d;
  }
  * { margin: 0; padding: 0; box-sizing: border-box; }
  html, body { width: 869px; height: 1200px; overflow: hidden; }
  body {
    background: var(--bg);
    font-family: "Montserrat", sans-serif;
    color: var(--text);
    position: relative;
  }
  .spread {
    position: absolute;
    left: 74px;
    width: 720px;
    height: 460px;
    display: flex;
    box-shadow: 0 18px 40px rgba(0,0,0,0.25);
  }
  .spread--outside { top: 110px; }
  .spread--inside { top: 630px; }
  .panel {
    width: 360px;
    height: 460px;
    position: relative;
    background: var(--card);
  }
  .panel--left { background: var(--card-dark); border-right: 1px solid #1a1a1a; }
  .photo {
    position: absolute;
    left: 0; bottom: 0;
    width: 360px; height: 190px;
    background: linear-gradient(135deg, var(--photo-a) 0%, var(--photo-b) 55%, var(--photo-a) 100%);
  }
  .panel-text {
    position: absolute;
    left: 34px; top: 40px; right: 34px;
  }
  .person-name {
    font-size: 22px;
    font-weight: 700;
    letter-spacing: 1px;
    text-transform: uppercase;
    color: var(--text);
  }
  .person-name .first { color: var(--gold); }
  .person-role {
    font-size: 11px;
    color: var(--muted);
    margin-top: 4px;
  }
  .social-icons { display: flex; gap: 8px; margin-top: 26px; }
  .social-icons span {
    width: 10px; height: 10px; border-radius: 50%;
    background: var(--gold);
  }
  .contact-list {
    list-style: none;
    margin-top: 18px;
    font-size: 11px;
    line-height: 1.9;
    color: var(--text);
  }
  .section-title {
    font-size: 20px;
    font-weight: 700;
    letter-spacing: 1.5px;
    text-transform: uppercase;
    color: var(--text);
  }
  .section-title .accent { color: var(--gold); }
  .specialty-list {
    list-style: none;
    margin-top: 30px;
    font-size: 12px;
    line-height: 2;
  }
  .brand {
    position: absolute;
    left: 50%; top: 50%;
    transform: translate(-50%, -50%);
    display: flex; align-items: center; gap: 12px;
  }
  .brand-mark { width: 22px; height: 22px; background: var(--gold); }
  .brand-name {
    font-size: 26px; font-weight: 700; letter-spacing: 3px;
    color: var(--gold);
  }
  .badge {
    position: absolute;
    left: 50%; top: 50%;
    transform: translate(-50%, -50%);
  }
</style>
</head>
<body>

  <section class="spread spread--outside">
    <div class="panel panel--left">
      <div class="panel-text">
        <h1 class="person-name"><span class="first">Jonas</span> Brenner</h1>
        <p class="person-role">Inhaber</p>
        <div class="social-icons"><span></span><span></span><span></span></div>
        <ul class="contact-list">
          <li>Hauptstraße 12</li>
          <li>54321 Talheim</li>
          <li>Tel. 0123 456789</li>
          <li>brenner-fleisch.de</li>
          <li>@brennerfleisch</li>
        </ul>
      </div>
      <div class="photo" role="img" aria-label="Schwarzweißfoto des Inhabers mit verschränkten Händen"></div>
    </div>
    <div class="panel panel--right">
      <div class="brand">
        <span class="brand-mark"></span>
        <span class="brand-name">BRENNER</span>
      </div>
    </div>
  </section>

  <section class="spread spread--inside">
    <div class="panel panel--left">
      <div class="panel-text">
        <h2 class="section-title"><span class="accent">Our</span> Specialty</h2>
        <ul class="specialty-list">
          <li>Dry Aged Beef</li>
          <li>Grillkurse &amp; Seminare</li>
          <li>Catering für Events</li>
        </ul>
      </div>
      <div class="photo" role="img" aria-label="Schwarzweißfoto des Inhabers mit verschränkten Händen"></div>
    </div>
    <div class="panel panel--right">
      <svg class="badge" width="120" height="120" viewBox="0 0 120 120" aria-hidden="true">
        <circle cx="60" cy="60" r="56" fill="var(--gold)"/>
        <circle cx="60" cy="60" r="42" fill="var(--card)"/>
      </svg>
    </div>
  </section>

</body>
</html>
```